Business Card, Letterhead, Envelopes, Thank you cards, Post Cards
Business cards and stationary for life coach
Professional
Silver Heron Guidance Studio
Marla Penrick, MA
4810 North Calloway Avenue
Suite C 240
Missoula, Montana 59417
silverheronguidance@mailbox-example.net
silverheronguidance-example.com
I would like to see 'Let Your Dreams Take Flight' on the front of the card. This is the tagline. Please use a compatible font with the logo.
'Dragonfly spends most of her life underwater until the day she discovers her wings and soars upon the wind.' I'd like to see this in script, similar to the logo font.
Please let me know if you need different files.

```html
<!DOCTYPE html>
<html lang="en">
<head>
<meta charset="utf-8">
<title>Silver Heron Guidance Studio — Stationery Set</title>
<link href="https://fonts.googleapis.com/css2?family=Great+Vibes&family=Open+Sans:wght@400;600&display=swap" rel="stylesheet">
<style>
  :root{
    --backdrop:#3a3b3d;
    --paper:#ffffff;
    --paper-soft:#f4f6f8;
    --brand-blue:#1f6fb8;
    --brand-deep:#134f8c;
    --brand-light:#4d9ad8;
    --ink:#4a4f55;
    --mist:#e3eef7;
  }
  *{box-sizing:border-box;margin:0;padding:0}
  html,body{width:1200px;height:313px;overflow:hidden;background:var(--backdrop);font-family:"Open Sans",Arial,sans-serif;color:var(--ink)}
  .set{position:relative;width:1200px;height:313px}
  .piece{position:absolute;background:var(--paper);box-shadow:0 2px 6px rgba(0,0,0,.45);overflow:hidden}
  .brand{font-family:"Great Vibes",cursive;color:var(--brand-blue);white-space:nowrap;line-height:1}
  .brand--light{color:var(--paper)}
  .tiny{font-size:4px;line-height:1.35;color:var(--ink)}
  .mark-dot{display:inline-block;border-radius:50%;background:var(--brand-blue);vertical-align:middle}

  /* standalone logo */
  .logo{position:absolute;left:28px;top:16px;width:120px;text-align:center}
  .logo .brand{font-size:22px}
  .logo .sub{font-size:6px;letter-spacing:1.5px;color:#dfe6ee;margin-top:4px;text-transform:uppercase}

  /* business cards */
  .card{width:101px;height:66px}
  .card .brand{position:absolute;left:8px;top:12px;font-size:11px}
  .card .tiny{position:absolute;left:8px;bottom:8px}
  .card--back{background:var(--paper)}
  .card--back .tagline{position:absolute;left:0;right:0;top:50%;transform:translateY(-50%);text-align:center;font-size:8px}
  .card--blue{background:linear-gradient(135deg,var(--brand-light),var(--brand-deep))}
  .card--blue .brand{color:var(--paper);left:50%;top:24px;transform:translateX(-50%)}
  .card--blue .tiny{color:#dcecf9;left:0;right:0;text-align:center;bottom:14px}
  .card .edge{position:absolute;right:0;top:0;bottom:0;width:5px;background:var(--brand-blue)}

  /* letterheads */
  .letter{top:19px;height:274px}
  .letter .brand{position:absolute;left:16px;top:18px;font-size:12px}
  .letter .contact{position:absolute;right:10px;top:16px;text-align:left}
  .letter .spine{position:absolute;left:0;top:0;bottom:0;width:5px;background:var(--brand-blue)}
  .letter .watermark{position:absolute;left:50%;top:48%;width:70px;height:70px;border-radius:50%;background:var(--mist);transform:translate(-50%,-50%)}
  .letter .footer{position:absolute;left:0;right:0;bottom:10px;text-align:center}

  /* envelopes */
  .env .brand{position:absolute;left:12px;top:10px;font-size:10px}
  .env .tiny{position:absolute;left:12px;top:24px}
  .env .stripe{position:absolute;left:0;top:0;bottom:0;width:5px;background:var(--brand-blue)}
  .env .watermark{position:absolute;right:16px;bottom:10px;width:34px;height:34px;border-radius:50%;background:var(--mist)}
  .env svg{position:absolute;inset:0}
</style>
</head>
<body>
<main class="set">

  <div class="logo">
    <div class="brand brand--light">Silver Heron</div>
    <div class="sub">Guidance Studio</div>
  </div>

  <!-- business cards -->
  <section class="piece card" style="left:14px;top:113px">
    <div class="brand">Silver Heron</div>
    <div class="tiny">Marla Penrick, MA<br>silverheronguidance-example.com</div>
    <span class="edge"></span>
  </section>
  <section class="piece card" style="left:120px;top:113px">
    <div class="brand" style="font-size:9px">Silver Heron</div>
    <div class="tiny">4810 North Calloway Avenue, Suite C 240<br>Missoula, Montana 59417<br>silverheronguidance@mailbox-example.net</div>
  </section>
  <section class="piece card card--back" style="left:14px;top:202px">
    <div class="brand tagline">Let Your Dreams Take Flight</div>
  </section>
  <section class="piece card card--blue" style="left:120px;top:202px">
    <div class="brand">Silver Heron</div>
    <div class="tiny">Let Your Dreams Take Flight</div>
  </section>

  <!-- letterheads -->
  <section class="piece letter" style="left:242px;width:161px">
    <span class="spine"></span>
    <div class="brand">Silver Heron</div>
    <div class="tiny contact">4810 North Calloway Avenue<br>Suite C 240<br>Missoula, Montana 59417</div>
    <div class="watermark"></div>
    <div class="tiny footer">silverheronguidance-example.com</div>
  </section>
  <section class="piece letter" style="left:422px;width:154px">
    <div class="brand" style="left:50%;transform:translateX(-50%);font-size:14px">Silver Heron</div>
    <div class="watermark"></div>
    <div class="tiny footer">4810 North Calloway Avenue · Suite C 240 · Missoula, Montana 59417</div>
  </section>

  <!-- small envelopes -->
  <section class="piece env" style="left:700px;top:29px;width:152px;height:86px">
    <span class="stripe"></span>
    <div class="brand">Silver Heron</div>
    <div class="tiny">4810 North Calloway Avenue<br>Suite C 240, Missoula, MT 59417</div>
    <div class="watermark"></div>
  </section>
  <section class="piece env" style="left:700px;top:173px;width:152px;height:86px">
    <div class="brand">Silver Heron</div>
    <div class="tiny">4810 North Calloway Avenue<br>Suite C 240, Missoula, MT 59417</div>
  </section>

  <!-- long envelopes -->
  <section class="piece env" style="left:864px;top:29px;width:302px;height:86px;background:var(--paper-soft)">
    <svg viewBox="0 0 302 86" width="302" height="86" preserveAspectRatio="none">
      <polygon points="0,0 302,0 151,56" fill="var(--brand-blue)"/>
      <polygon points="0,0 151,56 0,86" fill="#e8edf2"/>
      <polygon points="302,0 151,56 302,86" fill="#e8edf2"/>
    </svg>
    <span class="mark-dot" style="position:absolute;left:146px;top:50px;width:10px;height:10px;background:var(--paper)"></span>
  </section>
  <section class="piece env" style="left:876px;top:120px;width:292px;height:82px;background:var(--brand-blue)">
    <svg viewBox="0 0 292 82" width="292" height="82" preserveAspectRatio="none">
      <polygon points="0,30 146,70 292,30 292,82 0,82" fill="var(--paper)"/>
    </svg>
    <div class="brand brand--light" style="left:50%;top:8px;transform:translateX(-50%)">Silver Heron</div>
  </section>
  <section class="piece env" style="left:876px;top:205px;width:292px;height:78px">
    <span class="stripe"></span>
    <div class="brand">Silver Heron</div>
    <div class="tiny">4810 North Calloway Avenue<br>Suite C 240, Missoula, MT 59417</div>
  </section>

</main>
</body>
</html>
```